Halvorn Hire Business Card Design

Need business cards designed for our new equipment rental. We specialize in renting to landscape / tree professionals, contractors, Do-It-Yourself'ers and Around the home or office. Looking for a eye catching card. Landscape and construction should be the theme. The logo is attached, and you can see our colors from the logo. You can use whatever color goes with it ok.

Target Market(s)

First off Landscape and Tree Professional. Then contractors, Do-It-Yourself'ers and rentals for Around the home or office.

Industry/Entity Type

Business

Contact Information for Business Card

Eye catching background that blends landscaping with construction equipment

Requirements
Must have
• Name on Card will Be: Derek Pollard (Manager)
• My Direct Phone Number is: 352-418-7093
• derek@halvornhire.example
• www.halvornhire.example
• 4172 Wexley Mill Road,
• Dade City FL 33590
Nice to have
• Would be Nice to have these bullets on the Face of the card that does not have all my information.
• Serving:
• Landscape / Tree Professionals
• Contractors
• DYI'ers or say Do-It-Yourself'ers
• Maybe have serving small and centered above these bullets, and these 3 bullets along the bottom of the card. Ideas?

```html
<!DOCTYPE html>
<html lang="en">
<head>
<meta charset="utf-8">
<title>Halvorn Hire Business Card</title>
<link rel="stylesheet" href="https://fonts.googleapis.com/css2?family=Open+Sans:wght@400;600;700&display=swap">
<style>
  :root {
    --stage: #333333;
    --card: #ffffff;
    --navy: #0b3f6b;
    --grey: #9a9a9a;
    --ink: #1e1e1e;
  }
  * { box-sizing: border-box; margin: 0; padding: 0; }
  html, body { width: 1200px; height: 900px; overflow: hidden; }
  body {
    background: var(--stage);
    font-family: "Open Sans", Arial, sans-serif;
    color: var(--ink);
    position: relative;
  }
  .card {
    position: absolute;
    top: 306px;
    width: 440px;
    height: 271px;
    background: var(--card);
    overflow: hidden;
  }
  .card--front { left: 149px; }
  .card--back { left: 608px; }

  .footer-band { position: absolute; left: 0; bottom: 0; width: 440px; height: 20px; }

  .name-accent { position: absolute; left: 0; top: 26px; width: 30px; height: 38px; }
  .person { position: absolute; left: 36px; top: 31px; }
  .person__name {
    font-size: 14px; font-weight: 700; letter-spacing: 0.2px; line-height: 17px;
    color: var(--navy); text-transform: uppercase;
  }
  .person__name .surname { color: var(--grey); }
  .person__role { font-size: 11.5px; line-height: 15px; color: var(--ink); }

  .contact-list { position: absolute; left: 28px; top: 157px; list-style: none; }
  .contact-list li {
    display: flex; align-items: center; height: 16px;
    font-size: 11.5px; color: var(--ink); white-space: nowrap;
  }
  .contact-list svg { width: 10px; height: 10px; margin-right: 6px; fill: var(--navy); flex: none; }

  .address {
    position: absolute; right: 26px; top: 202px; text-align: right;
    font-size: 11.5px; line-height: 16px; font-style: normal; white-space: nowrap;
  }

  .brand {
    position: absolute; display: flex; align-items: center; gap: 8px;
    font-weight: 700; color: var(--navy); text-transform: uppercase; white-space: nowrap;
  }
  .brand__mark { background: var(--grey); }
  .card--front .brand { left: 202px; top: 118px; font-size: 24px; }
  .card--front .brand__mark { width: 14px; height: 14px; }
  .card--back .brand { left: 50%; top: 114px; transform: translateX(-50%); font-size: 30px; }
  .card--back .brand__mark { width: 18px; height: 18px; }
</style>
</head>
<body>

<section class="card card--front" aria-label="Card front">
  <svg class="name-accent" viewBox="0 0 30 38" aria-hidden="true">
    <polygon points="0,0 10,0 16,38 0,38" fill="var(--grey)"/>
    <polygon points="11,0 28,0 28,38 17,38" fill="var(--navy)"/>
  </svg>
  <div class="person">
    <p class="person__name">Derek <span class="surname">Pollard</span></p>
    <p class="person__role">Manager</p>
  </div>

  <div class="brand"><span class="brand__mark"></span>Halvorn Hire</div>

  <ul class="contact-list">
    <li><svg viewBox="0 0 10 10"><path d="M0 3 Q5 -1 10 3 L8 4.5 L6.5 3.5 L3.5 3.5 L2 4.5 Z M2 5 H8 V9 H2 Z"/></svg>352-418-7093</li>
    <li><svg viewBox="0 0 10 10"><rect x="2.5" y="0" width="5" height="10" rx="1"/><rect x="3.5" y="1.3" width="3" height="6" fill="#fff"/></svg>352-418-7093</li>
    <li><svg viewBox="0 0 10 10"><rect x="3" y="0" width="4" height="3"/><rect x="0.5" y="3" width="9" height="6" rx="1"/></svg>352-418-7093</li>
    <li><svg viewBox="0 0 10 10"><rect x="0" y="1.5" width="10" height="7"/><path d="M0 1.5 L5 5.5 L10 1.5" stroke="#fff" stroke-width="1" fill="none"/></svg>derek@halvornhire.example</li>
    <li><svg viewBox="0 0 10 10"><circle cx="5" cy="5" r="5"/><path d="M0 5 H10 M5 0 Q2 5 5 10 M5 0 Q8 5 5 10" stroke="#fff" stroke-width="0.7" fill="none"/></svg>www.halvornhire.example</li>
  </ul>

  <address class="address">4172 Wexley Mill Road,<br>Dade City FL 33590</address>

  <svg class="footer-band" viewBox="0 0 440 20" aria-hidden="true">
    <polygon points="0,6 217,6 209,20 0,20" fill="var(--grey)"/>
    <polygon points="222,2 440,2 440,20 208,20" fill="var(--navy)"/>
  </svg>
</section>

<section class="card card--back" aria-label="Card back">
  <div class="brand"><span class="brand__mark"></span>Halvorn Hire</div>
  <svg class="footer-band" viewBox="0 0 440 20" aria-hidden="true">
    <polygon points="0,6 217,6 209,20 0,20" fill="var(--grey)"/>
    <polygon points="222,2 440,2 440,20 208,20" fill="var(--navy)"/>
  </svg>
</section>

</body>
</html>
```